Flyer for Makeup Class

A flyer for my makeup class promotion. I am a make up artist starting a group class to teach makeup to ladies. I have attached some verbiage handwritten. My picture is the one in pink hijab. I have also attached some inspiration ideas and color combination (the colors in the cake design are the ones I want to use).

Target Market(s)

Ladies looking to learn make up from a make up artist

Industry/Entity Type

Hair And Beauty

Requirements
Must have
• The verbiage / description that I have hand written should be written using graphics and nice fonts. You can change the exact wording to make it better.

```html
<!DOCTYPE html>
<html lang="en">
<head>
<meta charset="UTF-8">
<title>Make Up Masterclass Flyer</title>
<link href="https://fonts.googleapis.com/css2?family=Kaushan+Script&family=Playfair+Display:ital,wght@1,700&family=Montserrat:wght@300;400;500&family=Oswald:wght@300;400;600&display=swap" rel="stylesheet">
<style>
  :root {
    --page: #f3f1f1;
    --paper: #ffffff;
    --rose: #c46c86;
    --blush: #efbcbc;
    --blush-deep: #e7a9ab;
    --gold: #d9a441;
    --ink: #1c1c1c;
    --grey: #6f6a6a;
    --script-grey: #5c5758;
    --white: #ffffff;
  }
  * { margin: 0; padding: 0; box-sizing: border-box; }
  html, body { width: 1200px; height: 1138px; overflow: hidden; background: var(--page); }
  .flyer {
    position: absolute; left: 210px; top: 17px;
    width: 780px; height: 1104px;
    background: var(--paper); overflow: hidden;
  }
  .frame-lines { position: absolute; inset: 0; }
  .powder { position: absolute; border-radius: 50%; filter: blur(2px); }
  .powder--top-right {
    right: -40px; top: -30px; width: 260px; height: 330px;
    background: radial-gradient(circle at 60% 40%, #b98a80 0%, #d8b3ab 35%, #f1dcd7 60%, rgba(255,255,255,0) 72%);
  }
  .powder--left {
    left: -70px; top: 260px; width: 230px; height: 320px;
    background: radial-gradient(circle at 40% 45%, #d98f9c 0%, #eab6be 40%, #f6dde1 60%, rgba(255,255,255,0) 72%);
  }
  .powder--bottom-left {
    left: -60px; top: 750px; width: 160px; height: 280px;
    background: radial-gradient(circle at 40% 50%, #a7606e 0%, #cf97a1 40%, rgba(255,255,255,0) 70%);
  }
  .headline { position: absolute; left: 0; width: 100%; text-align: center; }
  .headline__kicker {
    top: 60px; font-family: "Kaushan Script", cursive; font-size: 50px; color: var(--rose);
  }
  .headline__title {
    top: 126px; font-family: "Playfair Display", serif; font-style: italic; font-weight: 700;
    font-size: 26px; letter-spacing: 5px; color: var(--ink);
  }
  .headline__host {
    top: 188px; font-family: "Montserrat", sans-serif; font-weight: 400;
    font-size: 28px; letter-spacing: 5px; color: var(--ink);
  }
  .headline__credential {
    top: 228px; font-family: "Montserrat", sans-serif; font-weight: 400;
    font-size: 15px; letter-spacing: 3px; color: var(--ink);
  }
  .event-info {
    position: absolute; left: 226px; top: 310px; display: flex; align-items: center;
    font-family: "Oswald", sans-serif;
  }
  .event-info__day { font-size: 58px; font-weight: 600; color: var(--gold); line-height: 1; }
  .event-info__month {
    margin-left: 4px; margin-right: 12px; font-size: 20px; font-weight: 600; color: var(--gold);
    line-height: 1.15;
  }
  .event-info__venue { font-size: 19px; font-weight: 300; color: var(--ink); line-height: 1.4; letter-spacing: .5px; }
  .event-info__time { margin-left: 36px; }
  .audience-pill {
    position: absolute; left: 188px; top: 412px; width: 404px; height: 75px;
    background: var(--blush); border-radius: 12px;
    display: flex; align-items: center; justify-content: center; text-align: center;
    font-family: "Montserrat", sans-serif; font-weight: 500; font-size: 15.5px;
    letter-spacing: 1.5px; line-height: 1.45; color: var(--white);
  }
  .description {
    position: absolute; left: 130px; width: 520px; top: 530px; text-align: center;
    font-family: "Montserrat", sans-serif; font-weight: 300; font-size: 16px;
    letter-spacing: 1.6px; line-height: 1.8; color: var(--grey);
  }
  .portrait {
    position: absolute; left: 44px; top: 610px; width: 440px; height: 494px;
    border-radius: 220px 220px 0 0;
    background: linear-gradient(180deg, #fbe9ea 0%, #f4c8cc 45%, #e98fa7 80%, #d64f87 100%);
  }
  .booking { position: absolute; inset: 0; pointer-events: none; }
  .booking__title-script {
    position: absolute; left: 520px; top: 700px;
    font-family: "Kaushan Script", cursive; font-size: 64px; color: var(--script-grey);
  }
  .booking__title-bold {
    position: absolute; left: 520px; top: 775px;
    font-family: "Oswald", sans-serif; font-weight: 600; font-size: 56px; letter-spacing: 1px;
    color: var(--white); line-height: 1;
  }
  .contact {
    position: absolute; left: 482px; top: 862px; list-style: none;
    font-family: "Oswald", sans-serif; font-weight: 400; font-size: 23px; color: var(--white);
  }
  .contact__item { display: flex; align-items: center; height: 40px; }
  .contact__item--social { margin-top: 8px; }
  .contact__icon { width: 22px; height: 22px; margin-right: 22px; flex: none; }
  .contact__dot { width: 18px; height: 18px; margin: 0 24px 0 2px; background: var(--script-grey); border-radius: 4px; flex: none; }
</style>
</head>
<body>
  <main class="flyer">
    <svg class="frame-lines" width="780" height="1104" viewBox="0 0 780 1104" aria-hidden="true">
      <line x1="0" y1="170" x2="750" y2="0" stroke="#e2dada" stroke-width="1.5"/>
      <line x1="700" y1="0" x2="780" y2="600" stroke="#e2dada" stroke-width="1.5"/>
    </svg>

    <div class="powder powder--top-right" role="img" aria-label="Scattered eyeshadow and blush powder in rose and taupe tones"></div>
    <div class="powder powder--left" role="img" aria-label="Crushed pink blush powder"></div>
    <div class="powder powder--bottom-left" role="img" aria-label="Crushed mauve shimmer powder"></div>

    <p class="headline headline__kicker">Exclusive</p>
    <h1 class="headline headline__title">MAKE UP MASTERCLASS</h1>
    <p class="headline headline__host">BY NADIA RAHMAN</p>
    <p class="headline headline__credential">(UK BASED MUA)</p>

    <section class="event-info">
      <span class="event-info__day">6</span>
      <span class="event-info__month">APRIL<br>2019</span>
      <span class="event-info__venue">RIVERSIDE HALL, CEDAR COMPLEX<br>NORTHFIELD<span class="event-info__time">11:30 - 05:30 PM</span></span>
    </section>

    <p class="audience-pill">PERFECT FOR PROFESSIONALS,<br>BEGINNERS AND MAKE UP LOVERS</p>

    <p class="description">THIS CLASS IS PACKED WITH LOADS OF INFORMATION, TIPS, LIVE DEMOS, GOODIE BAG, CERTIFICATE, Q&amp;A, LUNCH AND MUCH MORE</p>

    <div class="portrait" role="img" aria-label="Portrait of the make up artist wearing a pink hijab"></div>

    <svg class="booking" width="780" height="1104" viewBox="0 0 780 1104" aria-hidden="true">
      <path d="M300 1104 C420 1080 520 1060 600 1040 L780 1010 L780 1104 Z" fill="#ffffff" opacity=".85"/>
      <circle cx="610" cy="865" r="222" fill="var(--blush-deep)"/>
      <circle cx="610" cy="865" r="198" fill="none" stroke="#ffffff" stroke-width="2" stroke-dasharray="7 7"/>
    </svg>

    <p class="booking__title-script">Book</p>
    <p class="booking__title-bold">NOW</p>

    <ul class="contact">
      <li class="contact__item">
        <svg class="contact__icon" viewBox="0 0 24 24" aria-hidden="true"><path fill="#5c5758" d="M6.6 10.8a15.1 15.1 0 0 0 6.6 6.6l2.2-2.2c.3-.3.7-.4 1-.2 1.1.4 2.3.6 3.6.6.6 0 1 .4 1 1V20c0 .6-.4 1-1 1A17 17 0 0 1 3 4c0-.6.4-1 1-1h3.5c.6 0 1 .4 1 1 0 1.3.2 2.5.6 3.6.1.3 0 .7-.2 1z"/></svg>
        0700123456
      </li>
      <li class="contact__item"><span class="contact__icon"></span>3000555123</li>
      <li class="contact__item contact__item--social"><span class="contact__dot"></span>@nadiarahmanmua</li>
    </ul>
  </main>
</body>
</html>
```